" O produto é um site na internet que usuário guarda seus link favoritos ou qualquer link que ele desejar. Ao inserir um novo link para guardar o sistema acessará o site ao qual esse link aponta e fará a leitura completa da página e salvará todas as palavras encontradas na página no banco de dados do sistema para futura pesquisa pelo usuário. Paralelamente a isso o sistema fará uma foto completa da página como se fosse uma cópia e salvará também essa foto no banco de dados do sistema para que o usuário possa vê-la sem a necessidade de acessar a página original. Ao se cadastrar no site o usuário poderá criar um grupo privado para compartilhar seus links públicos com esse grupo ou se desejar manter todos seus links em estado privado - onde somente ele tem acesso aos seus links. Seria legal o designer acessar o site provisório e se registrar para verificar na prática como o sistema funciona e ter uma idéia de como tudo funciona. "

```html
<!DOCTYPE html>
<html lang="pt-BR">
<head>
<meta charset="utf-8">
<title>Linkvault — cartão de visita</title>
<link rel="stylesheet" href="https://fonts.googleapis.com/css2?family=Open+Sans:wght@400;600;700&display=swap">
<style>
  :root {
    --page-bg: #e6e6e4;
    --card-white: #ffffff;
    --card-navy: #2c3440;
    --card-navy-light: #38414e;
    --ink-dark: #2b2f35;
    --ink-light: #ffffff;
    --accent-green: #4cc21f;
    --muted-grey: #c7cbd0;
  }
  * { box-sizing: border-box; margin: 0; padding: 0; }
  html, body {
    width: 1200px; height: 1200px; overflow: hidden;
    background: var(--page-bg);
    font-family: "Open Sans", Arial, sans-serif;
  }
  .sheet {
    width: 1200px; height: 1200px;
    display: flex; flex-direction: column; align-items: center; justify-content: center;
    gap: 60px;
  }
  .card {
    width: 910px; height: 520px;
    border-radius: 6px;
    box-shadow: 0 14px 34px rgba(0,0,0,.22);
    position: relative; overflow: hidden;
  }
  .card--front {
    background: var(--card-white);
    display: flex; align-items: center; justify-content: center;
  }
  .card--back {
    background: linear-gradient(160deg, var(--card-navy-light), var(--card-navy) 60%);
    color: var(--ink-light);
  }
  .brand {
    display: flex; align-items: center; gap: 16px;
    font-weight: 700; letter-spacing: 1px;
  }
  .brand__dot { border-radius: 50%; background: var(--accent-green); }
  .card--front .brand { font-size: 92px; color: var(--ink-dark); }
  .card--front .brand__dot { width: 34px; height: 34px; }
  .card--back .brand {
    position: absolute; right: 90px; top: 130px;
    font-size: 60px; color: var(--ink-light);
  }
  .card--back .brand__dot { width: 22px; height: 22px; }
  .holder { position: absolute; left: 90px; top: 150px; }
  .holder__name { font-size: 42px; line-height: 1.1; }
  .holder__name strong { font-weight: 700; }
  .holder__role { font-size: 22px; color: var(--accent-green); margin-top: 4px; }
  .contacts { position: absolute; left: 90px; top: 275px; list-style: none; }
  .contacts li {
    display: flex; align-items: center; gap: 22px;
    font-size: 26px; margin-bottom: 22px;
  }
  .contacts__icon {
    width: 44px; height: 44px; border-radius: 50%;
    background: var(--accent-green);
    display: flex; align-items: center; justify-content: center;
  }
</style>
</head>
<body>
<main class="sheet">
  <section class="card card--front">
    <div class="brand"><span class="brand__dot"></span>Linkvault</div>
  </section>

  <section class="card card--back">
    <div class="holder">
      <p class="holder__name"><strong>Nome</strong> Sobrenome</p>
      <p class="holder__role">cargo na empresa</p>
    </div>
    <ul class="contacts">
      <li>
        <span class="contacts__icon">
          <svg width="24" height="24" viewBox="0 0 24 24" aria-hidden="true"><path fill="#fff" d="M6.6 10.8a15 15 0 0 0 6.6 6.6l2.2-2.2c.3-.3.7-.4 1-.2 1.1.4 2.3.6 3.6.6.6 0 1 .4 1 1V20c0 .6-.4 1-1 1A17 17 0 0 1 3 4c0-.6.4-1 1-1h3.5c.6 0 1 .4 1 1 0 1.3.2 2.5.6 3.6.1.3 0 .7-.2 1z"/></svg>
        </span>+55 11 4000-1020
      </li>
      <li>
        <span class="contacts__icon">
          <svg width="24" height="24" viewBox="0 0 24 24" aria-hidden="true"><rect x="3" y="6" width="18" height="12" rx="1.5" fill="#fff"/><path d="M3.5 6.5 12 13l8.5-6.5" fill="none" stroke="#4cc21f" stroke-width="1.8"/></svg>
        </span>ola@linkvault
      </li>
      <li>
        <span class="contacts__icon">
          <svg width="24" height="24" viewBox="0 0 24 24" aria-hidden="true" fill="none" stroke="#fff" stroke-width="1.8"><circle cx="12" cy="12" r="8.5"/><ellipse cx="12" cy="12" rx="3.8" ry="8.5"/><path d="M3.5 12h17"/></svg>
        </span>www.linkvault.com.br
      </li>
    </ul>
    <div class="brand"><span class="brand__dot"></span>Linkvault</div>
  </section>
</main>
</body>
</html>
```